Host Home Needed Flier

We need a refresh of this flier to be more modern and informative. We'll use the new flier as a template for all our centers across the United States-therefore, it should be editable. We don't typically use stock photos (in order to look authentic to our clients) be would be open to a stock photo if it was relevant. We have a lot of work coming up and would like to establish a relationship with a designer. We are an international company who have been business for over 30 years working with international students ages 8-30. Our marketing/branding colors should be fresh and appeal to young people from all over the globe. We love the color blue in every shade and we love innovative cool fonts.

```html
<!DOCTYPE html>
<html lang="en">
<head>
<meta charset="utf-8">
<title>Host Home Needed Flier</title>
<link rel="stylesheet" href="https://fonts.googleapis.com/css2?family=Montserrat:wght@500;600;700&family=Poppins:wght@600;700;800&family=Roboto+Condensed:wght@300;400&display=swap">
<style>
  :root {
    --stage: #939ea6;
    --paper: #ffffff;
    --navy: #1b4a86;
    --blue: #1f5d9c;
    --panel: #1a5a98;
    --orange: #e8843a;
    --teal: #1aa99a;
    --teal-light: #9fdcd5;
    --orange-light: #f6c39a;
    --ink: #1b4a86;
  }
  * { margin: 0; padding: 0; box-sizing: border-box; }
  html, body { width: 1200px; height: 885px; overflow: hidden; }
  body { background: var(--stage); position: relative; font-family: "Montserrat", sans-serif; }

  .flier {
    position: absolute; top: 38px; width: 566px; height: 800px;
    background: var(--paper); overflow: hidden;
    box-shadow: 0 2px 8px rgba(0,0,0,.25);
    --accent: var(--teal); --accent-soft: var(--teal-light);
  }
  .flier--teal { left: 24px; }
  .flier--orange { left: 610px; --accent: var(--orange); --accent-soft: var(--orange-light); }

  .masthead { position: absolute; left: 0; top: 0; width: 100%; height: 90px; border-bottom: 5px solid var(--navy); }
  .masthead__mark { position: absolute; left: 29px; top: 21px; width: 54px; height: 54px; background: var(--navy); }
  .masthead__name { position: absolute; left: 96px; top: 30px; font-family: "Montserrat", sans-serif; font-weight: 700; font-size: 19.5px; letter-spacing: .6px; color: var(--navy); white-space: nowrap; }
  .masthead__tagline { position: absolute; left: 96px; top: 55px; font-weight: 500; font-size: 12.6px; letter-spacing: .3px; color: var(--navy); white-space: nowrap; }

  .hero-photo { position: absolute; left: 0; top: 95px; width: 100%; height: 268px; }
  .flier--teal .hero-photo { background: linear-gradient(180deg, #7fb2e6 0%, #b9d6f2 45%, #d3a58a 70%, #4a6fa8 100%); }
  .flier--orange .hero-photo { background: linear-gradient(180deg, #c9c2b4 0%, #a9857a 40%, #7da2c7 75%, #d9c37a 100%); }

  .headline { position: absolute; left: 0; top: 386px; width: 271px; text-align: center; font-family: "Poppins", sans-serif; font-weight: 700; font-size: 25.5px; line-height: 31px; color: var(--navy); }
  .headline__today { display: block; margin-top: 6px; font-size: 50px; line-height: 56px; font-weight: 800; color: var(--orange); letter-spacing: 1px; }

  .snapshots { position: absolute; left: 17px; top: 587px; width: 249px; height: 195px; display: grid; grid-template-columns: 121px 121px; grid-template-rows: 95px 94px; gap: 6px 7px; }
  .snapshots div:nth-child(1) { background: linear-gradient(160deg, #e9eef2, #b9c4cc 60%, #2b3540); }
  .snapshots div:nth-child(2) { background: linear-gradient(160deg, #5a8fd0, #c7a08a 55%, #3a2e2c); }
  .snapshots div:nth-child(3) { background: linear-gradient(160deg, #a48fa6, #c27a5c 55%, #2f5ea8); }
  .snapshots div:nth-child(4) { background: linear-gradient(160deg, #d9d7d0, #8a8d90 50%, #b8343a); }

  .info-panel { position: absolute; left: 271px; top: 363px; width: 295px; height: 339px; background: var(--panel); }
  .info-panel__photo { position: absolute; left: 1px; top: 17px; width: 278px; height: 156px; background: linear-gradient(150deg, #6f7d4a 0%, #c49c82 40%, #6a5a6e 70%, #3e4a66 100%); }
  .info-panel__text { position: absolute; left: 0; top: 183px; width: 295px; text-align: center; font-family: "Roboto Condensed", sans-serif; font-weight: 300; font-size: 25px; line-height: 30px; color: #fff; letter-spacing: .2px; }

  .stripe { position: absolute; left: 0; top: 0; }

  .pay-badge { position: absolute; left: 280px; top: 648px; width: 132px; height: 132px; }
  .pay-badge__text { position: absolute; left: 0; top: 28px; width: 132px; text-align: center; color: #fff; font-family: "Poppins", sans-serif; font-weight: 600; font-size: 23px; line-height: 25px; }
  .pay-badge__amount { display: block; font-size: 13px; font-weight: 700; line-height: 18px; }

  .contact { position: absolute; right: 18px; top: 741px; text-align: right; font-weight: 500; font-size: 15px; line-height: 20px; color: var(--navy); }
  .contact__line { display: flex; justify-content: flex-end; align-items: center; gap: 7px; }
  .contact__line svg { width: 13px; height: 13px; }
</style>
</head>
<body>

<article class="flier flier--teal">
  <header class="masthead">
    <div class="masthead__mark"></div>
    <div class="masthead__name">WORLDWAY STUDENT PLACEMENTS</div>
    <div class="masthead__tagline">Remarkable American Experiences for International Students</div>
  </header>
  <div class="hero-photo" role="img" aria-label="Photo of a diverse group of cheerful young students raising joined hands against a blue sky"></div>
  <h1 class="headline">BECOME A HOST<br>FOR AN<br>INTERNATIONAL<br>STUDENT<span class="headline__today">TODAY!</span></h1>
  <div class="snapshots">
    <div role="img" aria-label="Photo of host staff smiling in front of a classroom whiteboard"></div>
    <div role="img" aria-label="Photo of students posing together outdoors"></div>
    <div role="img" aria-label="Photo of students in sunglasses on a group trip"></div>
    <div role="img" aria-label="Photo of young students standing in a row"></div>
  </div>
  <section class="info-panel">
    <div class="info-panel__photo" role="img" aria-label="Photo of students studying together with a tablet outdoors"></div>
    <p class="info-panel__text">INTERNATIONAL STUDENTS<br>ATTENDING BCI ARRIVING<br>NOW!</p>
  </section>
  <svg class="stripe" width="566" height="800" viewBox="0 0 566 800" aria-hidden="true">
    <polygon points="400,702 566,702 566,717" fill="var(--accent)"/>
    <polygon points="420,706 566,718 566,726" fill="var(--accent-soft)"/>
  </svg>
  <div class="pay-badge">
    <svg width="132" height="132" viewBox="0 0 132 132" aria-hidden="true">
      <circle cx="66" cy="66" r="64" fill="var(--accent)"/>
      <circle cx="66" cy="66" r="57" fill="none" stroke="#fff" stroke-width="2"/>
    </svg>
    <div class="pay-badge__text">HOSTS<br>PAID<span class="pay-badge__amount">$1000/month</span></div>
  </div>
  <div class="contact">
    <div class="contact__line"><svg viewBox="0 0 24 24"><path d="M6.6 10.8a15.1 15.1 0 0 0 6.6 6.6l2.2-2.2a1 1 0 0 1 1-.25 11.4 11.4 0 0 0 3.6.57 1 1 0 0 1 1 1V20a1 1 0 0 1-1 1A17 17 0 0 1 3 4a1 1 0 0 1 1-1h3.5a1 1 0 0 1 1 1c0 1.25.2 2.45.57 3.57a1 1 0 0 1-.25 1z" fill="var(--orange)"/></svg>555-014-2290</div>
    <div class="contact__line"><svg viewBox="0 0 24 24" fill="none" stroke="var(--orange)" stroke-width="2"><circle cx="12" cy="12" r="10"/><path d="M2 12h20M12 2c3 3 3 17 0 20M12 2c-3 3-3 17 0 20"/></svg>worldwayhomes.com</div>
  </div>
</article>

<article class="flier flier--orange">
  <header class="masthead">
    <div class="masthead__mark"></div>
    <div class="masthead__name">WORLDWAY STUDENT PLACEMENTS</div>
    <div class="masthead__tagline">Remarkable American Experiences for International Students</div>
  </header>
  <div class="hero-photo" role="img" aria-label="Photo of a large diverse crowd of smiling young students seated together"></div>
  <h1 class="headline">BECOME A HOST<br>FOR AN<br>INTERNATIONAL<br>STUDENT<span class="headline__today">TODAY!</span></h1>
  <div class="snapshots">
    <div role="img" aria-label="Photo of host staff smiling in front of a classroom whiteboard"></div>
    <div role="img" aria-label="Photo of students posing together outdoors"></div>
    <div role="img" aria-label="Photo of students in sunglasses on a group trip"></div>
    <div role="img" aria-label="Photo of young students standing in a row"></div>
  </div>
  <section class="info-panel">
    <div class="info-panel__photo" role="img" aria-label="Photo of students studying together with a tablet outdoors"></div>
    <p class="info-panel__text">INTERNATIONAL STUDENTS<br>ATTENDING BCI ARRIVING<br>NOW!</p>
  </section>
  <svg class="stripe" width="566" height="800" viewBox="0 0 566 800" aria-hidden="true">
    <polygon points="400,702 566,702 566,717" fill="var(--accent)"/>
    <polygon points="420,706 566,718 566,726" fill="var(--accent-soft)"/>
  </svg>
  <div class="pay-badge">
    <svg width="132" height="132" viewBox="0 0 132 132" aria-hidden="true">
      <circle cx="66" cy="66" r="64" fill="var(--accent)"/>
      <circle cx="66" cy="66" r="57" fill="none" stroke="#fff" stroke-width="2"/>
    </svg>
    <div class="pay-badge__text">HOSTS<br>PAID<span class="pay-badge__amount">$1000/month</span></div>
  </div>
  <div class="contact">
    <div class="contact__line"><svg viewBox="0 0 24 24"><path d="M6.6 10.8a15.1 15.1 0 0 0 6.6 6.6l2.2-2.2a1 1 0 0 1 1-.25 11.4 11.4 0 0 0 3.6.57 1 1 0 0 1 1 1V20a1 1 0 0 1-1 1A17 17 0 0 1 3 4a1 1 0 0 1 1-1h3.5a1 1 0 0 1 1 1c0 1.25.2 2.45.57 3.57a1 1 0 0 1-.25 1z" fill="var(--orange)"/></svg>555-014-2290</div>
    <div class="contact__line"><svg viewBox="0 0 24 24" fill="none" stroke="var(--orange)" stroke-width="2"><circle cx="12" cy="12" r="10"/><path d="M2 12h20M12 2c3 3 3 17 0 20M12 2c-3 3-3 17 0 20"/></svg>worldwayhomes.com</div>
  </div>
</article>

</body>
</html>
```